General contractor/GM consaltant business card

I need a card for my contracting company in North Dakota, we build industrial buildings for the oil feild and oil feild related companies offices, shops, airplain hangars, airports ext. We have a familly atmosphere on the job and are very relational and personal.
Industry/Entity Type
Industrial
Contact Information for Business Card
Hollowpine Crafters LLC.
Dale T.Voskuijl
4873 Quenwick dr. Colorado Springs, CO. 80462
Cell# 406-738-1452
dale@hollowpinecrafters.example

```html
<!DOCTYPE html>
<html lang="en">
<head>
<meta charset="utf-8">
<title>Hollowpine Crafters LLC. – Business Card</title>
<link rel="stylesheet" href="https://fonts.googleapis.com/css2?family=Alegreya+Sans+SC:wght@500&family=PT+Sans:wght@400&display=swap">
<style>
  :root {
    --stage-light: #e6e7e8;
    --stage-dark: #b9babc;
    --card-white: #ffffff;
    --ink: #111111;
    --band: #000000;
    --gold: #ffcc11;
    --gold-soft: #fff1b8;
    --steel: #9a9b9e;
    --steel-light: #d5d6d8;
    --ghost: #f0f0f1;
    --icon-red: #c8102e;
    --on-band: #ffffff;
  }
  * { margin: 0; padding: 0; box-sizing: border-box; }
  html, body { width: 1200px; height: 1200px; overflow: hidden; }
  body {
    background: radial-gradient(circle at 50% 45%, var(--stage-light) 0%, var(--stage-light) 35%, var(--stage-dark) 100%);
    position: relative;
    font-family: "PT Sans", Arial, sans-serif;
  }
  .card { position: absolute; left: 228px; width: 742px; overflow: hidden; }
  .card--front { top: 172px; height: 422px; }
  .card--back { top: 600px; height: 424px; }

  .card__top { position: absolute; left: 0; top: 0; width: 742px; background: var(--card-white); }
  .card--front .card__top { height: 212px; }
  .card--back .card__top { height: 300px; }
  .card__band { position: absolute; left: 0; width: 742px; background: var(--band); }
  .card--front .card__band { top: 216px; height: 206px; }
  .card--back .card__band { top: 302px; height: 122px; }

  .wordmark { position: absolute; color: var(--ink); font-family: "Alegreya Sans SC", "PT Sans", sans-serif; font-weight: 500; line-height: 1; }
  .wordmark__main { display: block; font-size: 40px; letter-spacing: 1px; }
  .wordmark__sub { display: block; font-size: 25px; letter-spacing: 4px; margin-top: 2px; }
  .wordmark--front { left: 112px; top: 68px; }
  .wordmark--back { right: 50px; top: 28px; text-align: right; color: var(--on-band); }
  .brand-dot { position: absolute; border-radius: 50%; background: var(--gold); }
  .brand-dot--front { left: 22px; top: 66px; width: 76px; height: 76px; }

  .decor { position: absolute; left: 0; top: 0; }

  .holder-name {
    position: absolute; left: 30px; top: 86px;
    color: var(--on-band); font-family: "Alegreya Sans SC", "PT Sans", sans-serif;
    font-weight: 500; font-size: 27px; letter-spacing: 2px;
  }
  .contact { position: absolute; right: 20px; top: 22px; list-style: none; color: var(--on-band); font-size: 20px; line-height: 26px; text-align: right; }
  .contact__item { display: flex; justify-content: flex-end; align-items: flex-start; gap: 10px; }
  .contact__item + .contact__item { margin-top: 6px; }
  .contact__icon { flex: none; width: 20px; height: 20px; margin-top: 3px; }

  .back-logo-area { position: absolute; left: 66px; top: 24px; width: 230px; height: 250px; }
  .back-logo-area .brand-dot { left: 30px; top: 30px; width: 180px; height: 180px; }
</style>
</head>
<body>

<section class="card card--front" aria-label="Card front">
  <div class="card__top">
    <svg class="decor" width="742" height="212" viewBox="0 0 742 212" aria-hidden="true">
      <defs>
        <linearGradient id="goldFade" x1="0" y1="0" x2="1" y2="0">
          <stop offset="0" stop-color="var(--gold)"/>
          <stop offset="1" stop-color="var(--gold-soft)"/>
        </linearGradient>
      </defs>
      <path d="M430 212 C 520 170 580 140 640 60 L 742 60 L 742 212 Z" fill="var(--steel-light)"/>
      <path d="M0 196 L 430 196 C 480 180 540 140 570 118 L 572 124 C 540 150 490 188 440 208 L 0 208 Z" fill="url(#goldFade)"/>
    </svg>
    <div role="img" aria-label="Grey building towers illustration" style="position:absolute;left:612px;top:28px;width:130px;height:180px;background:linear-gradient(90deg,var(--steel) 0%,var(--steel-light) 100%);"></div>
    <span class="brand-dot brand-dot--front" aria-hidden="true"></span>
    <div class="wordmark wordmark--front">
      <span class="wordmark__main">Hollowpine</span>
      <span class="wordmark__sub">Crafters LLC.</span>
    </div>
  </div>
  <div class="card__band">
    <p class="holder-name">Dale T.Voskuijl</p>
    <ul class="contact">
      <li class="contact__item">
        <span>4873 Quenwick<br>Dr. Colorado Springs,<br>CO. 80462</span>
        <svg class="contact__icon" viewBox="0 0 20 20" aria-label="Address"><circle cx="10" cy="10" r="9" fill="var(--icon-red)" stroke="#fff" stroke-width="1.5"/><path d="M5 10 L10 5.5 L15 10 M7 9.5 V14 H13 V9.5" fill="none" stroke="#fff" stroke-width="1.6"/></svg>
      </li>
      <li class="contact__item">
        <span>406 - 738 - 1452</span>
        <svg class="contact__icon" viewBox="0 0 20 20" aria-label="Cell phone"><circle cx="10" cy="10" r="9" fill="var(--icon-red)" stroke="#fff" stroke-width="1.5"/><rect x="7" y="4.5" width="6" height="11" rx="1" fill="none" stroke="#fff" stroke-width="1.5"/><rect x="8.3" y="6" width="3.4" height="5" fill="#fff"/></svg>
      </li>
      <li class="contact__item" style="margin-top:0">
        <span>dale@hollowpinecrafters.example</span>
        <svg class="contact__icon" viewBox="0 0 20 20" aria-label="Email"><circle cx="10" cy="10" r="9" fill="var(--icon-red)" stroke="#fff" stroke-width="1.5"/><rect x="5" y="6.5" width="10" height="7" fill="none" stroke="#fff" stroke-width="1.4"/><path d="M5 6.5 L10 11 L15 6.5" fill="none" stroke="#fff" stroke-width="1.4"/></svg>
      </li>
    </ul>
  </div>
</section>

<section class="card card--back" aria-label="Card back">
  <div class="card__top">
    <div role="img" aria-label="Faint perspective skyscraper line illustration" style="position:absolute;left:0;top:0;width:742px;height:300px;background:linear-gradient(180deg,var(--card-white) 0%,var(--ghost) 55%,var(--card-white) 100%);"></div>
    <svg class="decor" width="742" height="300" viewBox="0 0 742 300" aria-hidden="true">
      <defs>
        <linearGradient id="goldLine" x1="0" y1="0" x2="1" y2="0">
          <stop offset="0" stop-color="var(--gold-soft)"/>
          <stop offset="0.25" stop-color="var(--gold)"/>
          <stop offset="1" stop-color="var(--gold)"/>
        </linearGradient>
      </defs>
      <rect x="382" y="287" width="360" height="10" fill="url(#goldLine)"/>
    </svg>
    <div class="back-logo-area"><span class="brand-dot" aria-hidden="true"></span></div>
  </div>
  <div class="card__band">
    <div class="wordmark wordmark--back">
      <span class="wordmark__main">Hollowpine</span>
      <span class="wordmark__sub">Crafters LLC.</span>
    </div>
  </div>
</section>

</body>
</html>
```